Company or website name
- zestoplex
- Links to the website
- www.zestoplex.com
- Describe your company and organization and target audience
- I need a website design for a new kids vitamins brand called ZESTOPLEX.   This brand is built on the foundations that it has everything you need, nothing that you dont (e.g. GMO, Animal Content, Soy, Dairy, Gelatin) and is right for everyone. This is a brand that appeals to millenial moms who want only the best for their kids.  It's colorful, bold, vibrant yet credible because all formulas are clinically tested.
- Other Facts

```html
<!DOCTYPE html>
<html lang="en">
<head>
<meta charset="UTF-8">
<title>Zestoplex — Set for Every Day</title>
<link href="https://fonts.googleapis.com/css2?family=Poppins:wght@500;600;700&display=swap" rel="stylesheet">
<style>
  :root {
    --page-bg: #ffffff;
    --ink-navy: #4a5694;
    --panel-top: #7fd6f3;
    --panel-mid: #6a7aa0;
    --panel-bottom: #574a6c;
    --arrow-cyan: #1fb2e0;
    --arrow-pink: #c872b0;
    --dot-pink: #f7d3e6;
    --dot-peach: #fbe0c8;
    --dot-lavender: #d2d3ec;
    --dot-mint: #d6eedd;
    --dot-lime: #e6f0d2;
    --dot-rose: #f8d2d6;
    --white: #ffffff;
  }
  * { margin: 0; padding: 0; box-sizing: border-box; }
  html, body { width: 1200px; height: 756px; overflow: hidden; background: var(--page-bg); }
  .hero {
    position: relative;
    width: 1200px;
    height: 756px;
    overflow: hidden;
    font-family: "Poppins", Arial, sans-serif;
    background: var(--page-bg);
  }
  .dot { position: absolute; border-radius: 50%; }
  .dot--pink { left: 1131px; top: 166px; width: 62px; height: 62px; background: var(--dot-pink); }
  .dot--peach-edge { left: 1159px; top: 353px; width: 72px; height: 82px; background: var(--dot-peach); }
  .dot--lavender { left: 1078px; top: 452px; width: 52px; height: 52px; background: var(--dot-lavender); }
  .dot--mint { left: 1154px; top: 536px; width: 50px; height: 50px; background: var(--dot-mint); }
  .dot--peach { left: 951px; top: 554px; width: 60px; height: 60px; background: var(--dot-peach); }
  .dot--lime { left: 1040px; top: 564px; width: 30px; height: 30px; background: var(--dot-lime); }
  .dot--rose { left: 1112px; top: 633px; width: 60px; height: 60px; background: var(--dot-rose); }

  .product-lineup {
    position: absolute;
    left: 188px;
    top: 116px;
    width: 904px;
    height: 360px;
    border-radius: 28px;
    background: linear-gradient(90deg, #f4c46e 0%, #7fcfb0 14%, #5cc4d6 28%, #8a86d8 50%, #c86bb8 66%, #e07a7e 82%, #ef9a5e 100%);
    opacity: 0.85;
  }

  .flavour-panel {
    position: absolute;
    left: 0;
    top: 479px;
    width: 387px;
    height: 231px;
    border-radius: 0 46px 46px 0;
    background: linear-gradient(150deg, var(--panel-top) 0%, var(--panel-mid) 38%, var(--panel-bottom) 100%);
    color: var(--white);
  }
  .flavour-panel__eyebrow {
    position: absolute; left: 116px; top: 37px;
    font-size: 13px; font-weight: 600; letter-spacing: 0.3px;
  }
  .flavour-panel__title {
    position: absolute; left: 116px; top: 63px;
    font-size: 36px; font-weight: 600; line-height: 42px;
    white-space: nowrap;
  }
  .flavour-panel__subtitle {
    position: absolute; left: 116px; top: 161px;
    font-size: 12px; font-weight: 500;
  }

  .flavour-connector {
    position: absolute; left: 361px; top: 538px; width: 104px; height: 4px;
  }
  .flavour-name {
    position: absolute; left: 489px; top: 516px;
    font-size: 36px; font-weight: 600; color: var(--ink-navy); letter-spacing: 1.2px;
    line-height: 46px; white-space: nowrap;
  }

  .buy-button {
    position: absolute; left: 537px; top: 594px; width: 153px; height: 59px;
    border-radius: 15px; background: var(--ink-navy); color: var(--white);
    font-size: 20px; font-weight: 600;
    display: flex; align-items: center; justify-content: center;
    text-decoration: none;
  }
  .carousel-arrow { position: absolute; top: 606px; width: 52px; height: 36px; }
  .carousel-arrow--prev { left: 467px; }
  .carousel-arrow--next { left: 711px; }
</style>
</head>
<body>
<main class="hero">
  <span class="dot dot--pink"></span>
  <span class="dot dot--peach-edge"></span>
  <span class="dot dot--lavender"></span>
  <span class="dot dot--mint"></span>
  <span class="dot dot--peach"></span>
  <span class="dot dot--lime"></span>
  <span class="dot dot--rose"></span>

  <div class="product-lineup" role="img" aria-label="Product photo: seven Zestoplex gummy vitamin bottles in a row with coloured caps, the purple-capped elderberry immunity bottle at the centre"></div>

  <section class="flavour-panel">
    <p class="flavour-panel__eyebrow">ELDERBERRY</p>
    <h1 class="flavour-panel__title">Set for<br>every day</h1>
    <p class="flavour-panel__subtitle">Immunity support</p>
  </section>

  <svg class="flavour-connector" viewBox="0 0 104 4" aria-hidden="true">
    <line x1="0" y1="2" x2="104" y2="2" stroke="#4a5694" stroke-width="3" stroke-dasharray="16 12"/>
  </svg>
  <p class="flavour-name">ELDERBERRY</p>

  <svg class="carousel-arrow carousel-arrow--prev" viewBox="0 0 52 36" aria-label="Previous">
    <path d="M48 18H10M24 4 8 18l16 14" fill="none" stroke="#1fb2e0" stroke-width="8" stroke-linecap="round" stroke-linejoin="round"/>
  </svg>
  <a class="buy-button" href="#">Buy now</a>
  <svg class="carousel-arrow carousel-arrow--next" viewBox="0 0 52 36" aria-label="Next">
    <path d="M4 18h38M28 4l16 14-16 14" fill="none" stroke="#c872b0" stroke-width="8" stroke-linecap="round" stroke-linejoin="round"/>
  </svg>
</main>
</body>
</html>
```